New Toothpaste brand needs a logo & packaging design

Our company is launching a new toothpaste and is looking for a logo and packaging design. The toothpaste brand is called Brivana. The packaging should have the same design quality as the major international brands, such as Lumora, Lumora Totalcare, Dentiva, Pexolo, Wind-rise, Marvest, etc. The dominant colors for our brand should be hues of blue, similar to other major brands. In addition, there should be a little bit of green to represent the "Fresh Mint Blast" flavor and the "Extracts of Aloe Vera" included in the ingredients.

There are typically 3 unique sides on a toothpaste box:

The face: Repeated on ~3 sides of the 4 faces of the box
The back: The 4th box face has the instructions for use, ingredients, company information, bar code/product info, and some branding elements.
The sides: Usually consisting of just the logo, flavor etc.

Please refer to existing brands such as Lumora, Lumora Total-care, and Dentiva for an example of typical box layout and elements.

Task Details:
Package Dimensions: 180 mm x 48 mm x 28 mm, 100 ml toothpaste tube
Brand Name: Brivana
Description: Fluoride Toothpaste
Flavor: Fresh Mint Blast
5 Actions: Protects against cavities and tartar, freshens breath, whitens teeth, and maintains healthy gums. These actions can also be made into a list like Lumora Total Care or Dentiva Max care. For instance, Strong Teeth, Fresh Breath, Whitening, Healthy Gums, Cavity and Tartar Protection.
Also contains whitening micro particles and extracts of aloe vera which may be highlighted on the package

Overall, the look should be high quality and with the same look and feel as the big brands mentioned previously. We do not have an existing logo for this brand. The face of the package is the most important element as it is often repeated on several sides and on the tube itself.

Please let me know if you have any questions.

I've attached some of our favorite big brand designs below. I would say the Lumora Total Care and Gleam vers

The logos I've seen so far for Brivana, have been a bit too bold. A little bold is okay, but just needs to be moderate. 

I would like the colors to be bright and appealing. I mentioned shades of blue being the major color, but green should also be highlighted as well, perhaps in a 80% blue to 20% green ratio. 

Target Market(s)

adult consumer of toothpaste, both female and male.

Industry/Entity Type

It Company

Requirements
Must have
• A logo with the brand name: Brivana
Description or sub text: Fluoride Toothpaste
Flavor: Fresh Mint Blast
A phrase or list describing the Toothpaste Actions: e.g., Protects against cavities and tartar, freshens breath, whitens teeth, and maintains healthy gums. Or as a list simialr to Lumora Total Care or Dentiva Max Care:
-Anti-cavity
-Anti-tartar
-Fresh breath
-Whitening
-Healthy Gums

Special ingredient of "whitening micro particles: and "extracts of aloe vera", which should also be highlighted.

The color should mostly be shades of blue, with only a little bit of green to accentuate the fresh mint blast flavor and aloe vera

Nice to have
• The design should really look good next to lumora total care, gleam pure, and dentiva max care. These are our favorite designs.
Should not have
• For aloe vera, there is no need to show the plant.

The Brivana logo shouldn't be too Bold. This should be appeal to all consumers, not just men.

```html
<!DOCTYPE html>
<html lang="en">
<head>
<meta charset="utf-8">
<title>Brivana Fluoride Toothpaste – Carton Dieline</title>
<link href="https://fonts.googleapis.com/css2?family=Lato:ital,wght@0,400;0,700;0,900;1,400;1,700&display=swap" rel="stylesheet">
<style>
  :root{
    --navy:#0b1f7c;
    --panel-blue:#1b1ba3;
    --flap-blue:#2626c2;
    --bright-blue:#1f6fe0;
    --cyan-glow:#bff3ff;
    --deep-green:#0c7a2a;
    --silver-light:#f2f4f8;
    --ink:#0c1a26;
    --instructions-bg:#d4f2fb;
    --tick:#e8a21c;
    --white:#ffffff;
  }
  *{margin:0;padding:0;box-sizing:border-box}
  html,body{width:1200px;height:820px;overflow:hidden;background:var(--white)}
  body{font-family:"Lato",sans-serif;position:relative}

  .dieline{position:absolute;left:0;top:0;width:1200px;height:820px}

  .brand-name{font-weight:700;color:var(--silver-light);letter-spacing:.5px;line-height:1;white-space:nowrap}

  /* back panel */
  .back-panel{position:absolute;left:180px;top:108px;width:835px;height:227px;color:var(--white)}
  .instructions-box{position:absolute;left:35px;top:29px;width:365px;height:178px;background:var(--instructions-bg);border-radius:20px;color:var(--ink);font-size:13px;text-align:center;padding-top:12px}
  .ingredients{position:absolute;left:410px;top:34px;width:370px;font-size:13px;line-height:1.3;text-align:center}
  .branding-note{position:absolute;left:423px;top:100px;font-size:13px}
  .back-panel .brand-name{position:absolute;left:440px;top:146px;font-size:36px}
  .back-panel .descriptor{position:absolute;left:522px;top:190px;font-size:13px;font-weight:700;white-space:nowrap}

  /* front panels */
  .face{position:absolute;left:180px;width:835px;overflow:hidden;color:var(--white);
    background:
      radial-gradient(ellipse 190px 120px at 380px 50%,var(--cyan-glow) 0%,rgba(120,220,255,.55) 30%,rgba(31,111,224,0) 75%),
      linear-gradient(90deg,var(--navy) 0%,#1340b8 30%,var(--bright-blue) 45%,#28a6d6 62%,#2bb57a 80%,var(--deep-green) 100%);}
  .face-strip{height:130px}
  .face-strip.top{top:335px;border-bottom:1px dashed #333}
  .face-strip.bottom{top:685px}
  .face-main{top:465px;height:220px;border-bottom:1px dashed #333}
  .face svg{position:absolute;left:0;top:0}
  .face .abs{position:absolute;white-space:nowrap}

  .face-strip .brand-name{left:36px;top:16px;font-size:36px}
  .face-strip .descriptor{left:148px;top:59px;font-size:16px;font-weight:700}
  .face-strip .mint-art{left:38px;top:84px;width:44px;height:32px}
  .face-strip .flavor{left:86px;top:84px;font-size:15px;font-weight:700}
  .face-strip .flavor i{font-weight:400;font-style:italic}
  .face-strip .highlight{left:83px;top:105px;font-size:11px}
  .face-strip .net-weight{left:477px;top:105px;font-size:12px;color:var(--ink)}
  .face-strip .benefit{font-weight:900;color:var(--ink)}
  .face-strip .smile-art{left:412px;top:58px;width:66px;height:64px;border:4px solid #cfe9ff}

  .mint-art{border-radius:50% 40% 50% 45%;background:radial-gradient(circle at 40% 40%,#c9f3c0,#5cc45a 55%,#2d8a3a)}
  .smile-art{border-radius:50%;background:radial-gradient(circle at 45% 45%,#ffffff 0%,#e6736a 30%,#1f6fe0 62%,#0b3aa8 100%)}

  .face-main .brand-name{left:40px;top:26px;font-size:70px}
  .face-main .descriptor{left:218px;top:90px;font-size:17px;font-weight:700}
  .face-main .mint-art{left:45px;top:140px;width:70px;height:58px}
  .face-main .flavor{left:130px;top:137px;font-size:18px;font-weight:700}
  .face-main .with{left:188px;top:158px;font-size:13px;font-style:italic}
  .face-main .highlight{font-size:13px}
  .face-main .benefit{font-size:16px;color:var(--ink)}
  .face-main .tick{font-size:13px;color:var(--tick);font-weight:700}
  .face-main .benefits-seal{left:378px;top:28px;width:240px;height:180px;border-radius:50%;
    transform:rotate(-20deg);
    background:radial-gradient(ellipse at 50% 50%,#1a2f9a 0%,var(--navy) 55%,#9aa3b5 72%,#e9edf4 85%,rgba(233,237,244,0) 100%)}

  /* side flaps */
  .side-logo{position:absolute;transform:rotate(90deg);transform-origin:center;font-size:36px}
</style>
</head>
<body>

<svg class="dieline" viewBox="0 0 1200 820" aria-hidden="true">
  <defs>
    <linearGradient id="silver" x1="0" y1="0" x2="1" y2="1">
      <stop offset="0" stop-color="#ffffff"/>
      <stop offset=".5" stop-color="#c9cfdb"/>
      <stop offset="1" stop-color="#8e97aa"/>
    </linearGradient>
  </defs>
  <polygon points="180,108 237,57 958,57 1015,108" fill="#fff" stroke="#111" stroke-width="1.2"/>
  <rect x="180" y="108" width="835" height="227" fill="var(--panel-blue)"/>
  <line x1="180" y1="335" x2="1015" y2="335" stroke="#8899cc" stroke-dasharray="4 3"/>
  <path d="M1015 113 H1140 Q1148 113 1148 121 V128 H1170 Q1180 128 1180 140 V314 Q1180 326 1170 326 H1148 V328 Q1148 335 1140 335 H1015 Z" fill="var(--flap-blue)" stroke="#111" stroke-width="1"/>
  <line x1="1145" y1="128" x2="1145" y2="326" stroke="#111" stroke-dasharray="3 3"/>
  <circle cx="1047" cy="225" r="7" fill="none" stroke="#111"/>
  <path d="M180 340 L122 344 Q105 346 105 360 V448 Q105 460 122 460 L180 462 Z" fill="var(--flap-blue)" stroke="#111"/>
  <line x1="122" y1="344" x2="122" y2="460" stroke="#111" stroke-dasharray="3 3"/>
  <path d="M180 465 H38 Q20 465 20 480 V668 Q20 685 38 685 H180 Z" fill="var(--flap-blue)" stroke="#111"/>
  <line x1="56" y1="468" x2="56" y2="682" stroke="#111" stroke-dasharray="3 3"/>
  <circle cx="152" cy="575" r="7" fill="none" stroke="#111"/>
  <path d="M180 692 L122 696 Q105 698 105 712 V798 Q105 810 122 810 L180 812 Z" fill="var(--flap-blue)" stroke="#111"/>
  <line x1="122" y1="696" x2="122" y2="810" stroke="#111" stroke-dasharray="3 3"/>
</svg>

<section class="back-panel">
  <div class="instructions-box">Instructions for use</div>
  <p class="ingredients">Ingredients: all ingredients will be written on this section only only this section section asection section</p>
  <p class="branding-note">Other Branding elements here</p>
  <span class="brand-name">Brivana</span>
  <span class="descriptor">Fluoride Toothpaste</span>
</section>

<span class="side-logo brand-name" style="left:1038px;top:240px">Brivana</span>
<span class="side-logo brand-name" style="left:40px;top:582px">Brivana</span>

<section class="face face-strip top">
  <svg width="835" height="130" viewBox="0 0 835 130" aria-hidden="true">
    <path d="M360 130 Q430 40 640 8 L835 2 L835 10 Q580 34 402 130 Z" fill="url(#silver)"/>
  </svg>
  <span class="abs brand-name">Brivana</span>
  <span class="abs descriptor">Fluoride Toothpaste</span>
  <div class="abs mint-art" role="img" aria-label="Mint leaves with an aloe drop"></div>
  <span class="abs flavor">Fresh Mint Blast <i>with</i></span>
  <span class="abs highlight">whitening micro particles and extracts of aloe vera</span>
  <div class="abs smile-art" role="img" aria-label="Round badge with a toothbrush brushing a bright smile"></div>
  <span class="abs net-weight">NET WEIGHT: 100 ml</span>
  <span class="abs benefit" style="left:636px;top:16px;font-size:15px">Strong Teeth</span>
  <span class="abs benefit" style="left:691px;top:35px;font-size:14px">Fresh Breath</span>
  <span class="abs benefit" style="left:646px;top:52px;font-size:14px">Whitening</span>
  <span class="abs benefit" style="left:696px;top:66px;font-size:17px">Healthy Gums</span>
  <span class="abs benefit" style="left:615px;top:87px;font-size:14px">Cavity and Tartar Protection</span>
</section>

<section class="face face-main">
  <svg width="835" height="220" viewBox="0 0 835 220" aria-hidden="true">
    <path d="M330 220 Q420 60 640 12 L835 3 L835 14 Q590 40 390 220 Z" fill="url(#silver)"/>
  </svg>
  <div class="abs benefits-seal" role="img" aria-label="Five benefits seal"></div>
  <span class="abs brand-name">Brivana</span>
  <span class="abs descriptor">Fluoride Toothpaste</span>
  <div class="abs mint-art" role="img" aria-label="Mint leaves with an aloe vera drop"></div>
  <span class="abs flavor">Fresh Mint Blast</span>
  <span class="abs with">with</span>
  <span class="abs highlight" style="left:130px;top:176px">whitening micro particles</span>
  <span class="abs highlight" style="left:150px;top:192px">extracts of aloe vera</span>

  <span class="abs tick" style="left:612px;top:28px">✓</span>
  <span class="abs benefit" style="left:657px;top:25px">Strong Teeth</span>
  <span class="abs tick" style="left:632px;top:64px">✓</span>
  <span class="abs benefit" style="left:672px;top:61px">Fresh Breath</span>
  <span class="abs tick" style="left:642px;top:103px">✓</span>
  <span class="abs benefit" style="left:680px;top:100px">Whitening</span>
  <span class="abs tick" style="left:630px;top:146px">✓</span>
  <span class="abs benefit" style="left:658px;top:143px">Healthy Gums</span>
  <span class="abs tick" style="left:590px;top:185px">✓</span>
  <span class="abs benefit" style="left:606px;top:183px">Cavity and Tartar Protection</span>
</section>

<section class="face face-strip bottom">
  <svg width="835" height="130" viewBox="0 0 835 130" aria-hidden="true">
    <path d="M360 130 Q430 40 640 8 L835 2 L835 10 Q580 34 402 130 Z" fill="url(#silver)"/>
  </svg>
  <span class="abs brand-name">Brivana</span>
  <span class="abs descriptor">Fluoride Toothpaste</span>
  <div class="abs mint-art" role="img" aria-label="Mint leaves with an aloe drop"></div>
  <span class="abs flavor">Fresh Mint Blast <i>with</i></span>
  <span class="abs highlight">whitening micro particles and extracts of aloe vera</span>
  <div class="abs smile-art" role="img" aria-label="Round badge with a toothbrush brushing a bright smile"></div>
  <span class="abs net-weight">NET WEIGHT: 100 ml</span>
  <span class="abs benefit" style="left:633px;top:20px;font-size:15px">Strong Teeth</span>
  <span class="abs benefit" style="left:688px;top:39px;font-size:14px">Fresh Breath</span>
  <span class="abs benefit" style="left:643px;top:56px;font-size:14px">Whitening</span>
  <span class="abs benefit" style="left:693px;top:70px;font-size:17px">Healthy Gums</span>
  <span class="abs benefit" style="left:611px;top:91px;font-size:14px">Cavity and Tartar Protection</span>
</section>

</body>
</html>
```